Business Card - connecting 2 souls and beggining the journey of self discovery

Logo on the front
with tag line

On the back list of services and contact details

Seminars
workshops
Coaching
podcasts

Daniel Porthwick
Health & Wellbeing Life Coach
0491 372 815
daniel@wovenpathwellness.example
wovenpathwellness.example

Industry/Entity Type

Life Coaching

Contact Information for Business Card

I like the use of colour from the logo to be used. I'm not a fan of white.

Requirements
Must have
• My tagline: The journey home starts with you
Nice to have
• Use of colour that is in the Woven Path logo

```html
<!DOCTYPE html>
<html lang="en">
<head>
<meta charset="utf-8">
<title>Woven Path Wellness – Business Card</title>
<link rel="stylesheet" href="https://fonts.googleapis.com/css2?family=Quicksand:wght@500;600;700&display=swap">
<style>
  :root {
    --stage: #1c1c1e;
    --paper: #eef0f1;
    --green: #6fb41c;
    --green-light: #86c92a;
    --green-dark: #5a9915;
    --green-ink: #3f6e0f;
    --charcoal: #434345;
    --charcoal-light: #58585b;
    --ink: #3a3a3c;
    --white: #ffffff;
    --brand-dot: #f0902a;
  }
  html, body {
    margin: 0;
    width: 1042px;
    height: 1200px;
    overflow: hidden;
    background: var(--stage);
  }
  .canvas {
    position: relative;
    width: 1042px;
    height: 1200px;
  }
  .card {
    position: absolute;
    left: 81px;
    width: 880px;
    height: 502px;
    box-shadow: 0 10px 30px rgba(0,0,0,.45);
  }
  .card--back  { top: 64px; }
  .card--front { top: 634px; }
  .card svg { display: block; width: 100%; height: 100%; }
  .type { font-family: "Quicksand", sans-serif; }
  .name { font-size: 23px; font-weight: 700; fill: var(--white); }
  .role { font-size: 12px; font-weight: 500; fill: var(--green-ink); }
  .contact { font-size: 13px; font-weight: 600; fill: var(--white); }
  .tagline { font-size: 16.5px; font-weight: 600; fill: var(--white); }
  .service { font-size: 13px; font-weight: 600; fill: var(--white); }
  .brand-small { font-size: 15px; font-weight: 700; fill: var(--white); }
  .brand-large { font-size: 34px; font-weight: 700; fill: var(--ink); }
</style>
</head>
<body>
<main class="canvas">

  <!-- Back of card: contact details and services -->
  <section class="card card--back" aria-label="Business card back">
    <svg viewBox="0 0 626 357" xmlns="http://www.w3.org/2000/svg" class="type">
      <rect width="626" height="357" fill="var(--paper)"/>

      <!-- charcoal panel -->
      <polygon points="258,0 626,0 626,357 333,357" fill="var(--charcoal)"/>
      <polygon points="258,0 290,0 340,357 333,357" fill="var(--charcoal-light)"/>

      <!-- name band -->
      <rect x="0" y="68" width="284" height="62" fill="var(--green)"/>
      <polygon points="270,68 300,135 284,130" fill="var(--green-dark)"/>
      <text class="name" x="24" y="99">Daniel <tspan fill="var(--ink)">Porthwick</tspan></text>
      <text class="role" x="24" y="118">Health &amp; Wellbeing Life Coach</text>

      <!-- tagline band -->
      <polygon points="270,68 626,56 626,165 300,135" fill="var(--green)"/>
      <polygon points="270,68 300,135 286,72" fill="var(--green-light)"/>
      <text class="tagline" x="610" y="116" text-anchor="end">The journey home starts with you</text>

      <!-- services -->
      <g class="services">
        <circle cx="389" cy="193" r="2.5" fill="var(--green-light)"/>
        <text class="service" x="398" y="198">Seminars</text>
        <circle cx="389" cy="222" r="2.5" fill="var(--green-light)"/>
        <text class="service" x="398" y="227">Workshops</text>
        <circle cx="509" cy="193" r="2.5" fill="var(--green-light)"/>
        <text class="service" x="518" y="198">Coaching</text>
        <circle cx="509" cy="222" r="2.5" fill="var(--green-light)"/>
        <text class="service" x="518" y="227">Podcasts</text>
      </g>

      <!-- brand mark -->
      <g class="brand">
        <circle cx="468" cy="292" r="8" fill="var(--brand-dot)"/>
        <text class="brand-small" x="482" y="297">Woven Path</text>
      </g>

      <!-- contact bands -->
      <g class="contacts">
        <rect x="0" y="180" width="315" height="38" fill="var(--green)"/>
        <rect x="0" y="226" width="320" height="39" fill="var(--green)"/>
        <rect x="0" y="272" width="324" height="38" fill="var(--green)"/>

        <!-- phone -->
        <circle cx="34" cy="199" r="12" fill="none" stroke="var(--white)" stroke-width="1.5"/>
        <path d="M29,192 q-2,4 2,9 q4,5 9,4 l1,-3 l-3,-2 l-2,1 q-4,-2 -5,-6 l1,-2 l-2,-3 z" fill="var(--white)"/>
        <text class="contact" x="58" y="204">0491 372 815</text>

        <!-- email -->
        <circle cx="34" cy="245" r="12" fill="none" stroke="var(--white)" stroke-width="1.5"/>
        <rect x="27" y="240" width="14" height="10" fill="none" stroke="var(--white)" stroke-width="1.4"/>
        <path d="M27,240 l7,6 l7,-6" fill="none" stroke="var(--white)" stroke-width="1.4"/>
        <text class="contact" x="58" y="250">daniel@wovenpathwellness.example</text>

        <!-- web -->
        <circle cx="34" cy="291" r="12" fill="none" stroke="var(--white)" stroke-width="1.5"/>
        <circle cx="34" cy="291" r="7" fill="none" stroke="var(--white)" stroke-width="1.4"/>
        <path d="M27,291 h14 M34,284 v14" stroke="var(--white)" stroke-width="1.2"/>
        <text class="contact" x="58" y="296">wovenpathwellness.example</text>
      </g>
    </svg>
  </section>

  <!-- Front of card: brand and tagline -->
  <section class="card card--front" aria-label="Business card front">
    <svg viewBox="0 0 626 357" xmlns="http://www.w3.org/2000/svg" class="type">
      <rect width="626" height="357" fill="var(--paper)"/>

      <!-- brand mark -->
      <g class="brand">
        <circle cx="170" cy="123" r="16" fill="var(--brand-dot)"/>
        <text class="brand-large" x="198" y="135">Woven Path</text>
      </g>

      <!-- lower bands -->
      <polygon points="0,284 272,280 288,332 0,330" fill="var(--green)"/>
      <polygon points="272,280 294,290 310,357 288,332" fill="var(--green-dark)"/>
      <polygon points="292,290 626,142 626,357 308,357" fill="var(--green)"/>
      <polygon points="292,290 626,142 626,180 300,300" fill="var(--green-light)"/>

      <text class="tagline" x="606" y="324" text-anchor="end">The journey home starts with you</text>
    </svg>
  </section>

</main>
</body>
</html>
```